New look and feel for investment website

Hi

Our website needs a crisp and professional look and feel applying to it. Here’s the address: http://www.brightplinth.co.uk. Since posting the brief yesterday (Tuesday, 16 August), we've reduced the amount of content on the home page, which should make life a little easier for you. We will come back later today, with some points of reference in terms of sites we like the look of. (See below)

17 August, 1.20pm GMT. OK, comments generally on the designs submitted so far. Please keep in mind that images of graphs, piles of coins, paper money and pretty females are not what is required. Better to think in terms of abstract imagery instead. Ratios? Circles? Relationships? Patterns? Not money,sex,graphs etc. Hope that helps.

For guidance on look and feel, please refer to these sites, which we like:

http://www.morvelle.co.uk/
http://www.qz.com/
https://www.harrowfieldtamsin.com
https://www.pirelconcerns.com
https://www.kvantule.com
Updates

Here's the Tall Beacons logo created in AI CS5.

Our market is professional financial advisers and relatively sophisticated private investors. The look and feel therefore should be slick and sophisticated - not 'lively' and lightweight, more like a banking site. Please read the brief again where we've added a list of websites that we really like the look of to get a better feel for what we're looking for. Thanks once again, we appreciate the work you're putting in.

It's essential that all the elements that are on the current home page be included on all new designs. 

We use a device in our e-mails which you may wish to incorporate in your design.

Target Market(s)

Professional financial advisers. People who know about investment and money.

Industry/Entity Type

Investment

Requirements
Should not have
• Graphs or people.

```html
<!DOCTYPE html>
<html lang="en">
<head>
<meta charset="utf-8">
<title>Tall Beacons — Value Investing</title>
<link href="https://fonts.googleapis.com/css2?family=Open+Sans:ital,wght@0,400;0,600;0,700;1,700&family=Oswald:wght@400&family=Share+Tech+Mono&display=swap" rel="stylesheet">
<style>
:root{
  --ochre:#d9aa62;
  --ochre-soft:#f0d7ad;
  --nav-text:#35291a;
  --brand-text:#3d3a36;
  --brown-head:#7d6a3a;
  --body-text:#2b2b2b;
  --red:#c8161c;
  --red-deep:#9c0e12;
  --panel-bg:#f1efe8;
  --panel-head:#77706a;
  --footer-grey:#cbcbcb;
  --strip:rgba(120,104,84,.8);
}
*{margin:0;padding:0;box-sizing:border-box}
html,body{width:1200px;height:1082px;overflow:hidden;background:#fff}
body{position:relative;font-family:"Open Sans",Arial,sans-serif;color:var(--body-text)}
.abs{position:absolute}

.brand{left:14px;top:50px;font-size:34px;font-weight:400;color:var(--brand-text);letter-spacing:-.5px;line-height:40px}

.main-nav{left:280px;top:4px;width:913px;height:138px;background:var(--ochre);font-size:15.5px;color:var(--nav-text)}
.main-nav .col{position:absolute;top:18px;display:flex;flex-direction:column;gap:14px}
.main-nav .col a{color:var(--nav-text);text-decoration:none;line-height:23px;padding:0 11px;white-space:nowrap}
.main-nav .sep{position:absolute;top:12px;height:112px;border-left:1px dotted #7a5a28}
.main-nav .current{background:var(--ochre-soft)}

.hero{left:5px;top:142px;width:1188px;height:352px;overflow:hidden;
  background:radial-gradient(ellipse at 70% 60%,#b9a48a 0%,#8c7a66 22%,transparent 40%),
  radial-gradient(ellipse at 95% 40%,#d9b29e 0%,#c09480 20%,transparent 38%),
  linear-gradient(160deg,#5a4534 0%,#3a2b20 45%,#4a3a2c 100%)}
.util{right:0;top:0;width:913px;height:40px;background:var(--strip);display:flex;justify-content:flex-end;align-items:center;padding-right:10px;font-size:15px;font-weight:700;color:#fff}
.util span{padding:0 8px}
.util i{font-style:normal;font-weight:400}
.hero h1{left:45px;top:92px;width:640px;font-size:31px;line-height:41px;font-weight:700;color:#fff;text-shadow:0 1px 3px rgba(0,0,0,.5)}
.hero .cta{left:49px;top:270px;width:314px;height:56px;background:var(--red);color:#fff;font-family:"Share Tech Mono",monospace;font-size:25px;letter-spacing:1px;display:flex;align-items:center;justify-content:center}

.intro{left:8px;top:512px}
.intro h2{font-size:32px;font-weight:400;color:var(--brown-head);line-height:40px}
.intro p{width:780px;margin-top:10px;font-size:14.6px;line-height:20.5px}

.feature{top:644px}
.feature h3{font-size:21px;font-weight:400;color:#333;display:flex;align-items:center;gap:8px;line-height:30px}
.feature p{font-size:14.6px;line-height:20.5px;margin-top:2px}
.more{display:inline-block;margin-top:14px;background:var(--ochre);color:#fff;font-size:12.5px;font-weight:700;font-style:italic;padding:2px 18px 2px 8px;clip-path:polygon(0 0,88% 0,100% 50%,88% 100%,0 100%)}

.signup{left:826px;top:518px;width:366px;height:245px;background:var(--panel-bg)}
.signup h4{height:52px;background:var(--panel-head);color:#fff;font-size:21px;font-weight:400;padding:12px 14px;clip-path:polygon(0 0,95% 0,100% 22%,100% 100%,0 100%)}
.signup p{padding:14px 12px 0;font-size:14.6px;line-height:20.5px;color:#2b2b2b;text-align:justify}
.signup .trial{color:#a5121b}
.signup .link{color:#7d6030;font-weight:700;font-style:italic;text-decoration:underline}
.register{left:12px;top:164px;width:252px;height:50px;background:linear-gradient(#dc2228,var(--red-deep));border:1px solid #700a0d;color:#fff;font-family:"Oswald",sans-serif;font-size:24px;display:flex;align-items:center;padding-left:20px}
.register .arrow{position:absolute;right:0;top:0;width:46px;height:48px;background:linear-gradient(#6a0508,#340203);display:flex;align-items:center;justify-content:center}

.site-map{left:5px;top:854px;width:1188px;height:173px;background:var(--footer-grey);padding:30px 16px;font-size:15px;line-height:20.5px;color:#222}
.site-map .q{margin-top:20px}
.site-map .mark{position:absolute;right:10px;bottom:10px;font-size:22px;color:#555;line-height:26px}
.legal{left:5px;top:1027px;width:1188px;height:49px;background:var(--ochre);font-family:Arial,sans-serif;font-size:15px;color:#5e4620;display:flex;align-items:center;padding-left:16px}
.legal u{font-weight:700;font-style:italic;margin-left:5px}
.social{position:absolute;right:10px;top:12px;display:flex;gap:6px}
.social span{width:24px;height:24px;background:#5e4a30;border:1px solid #3e2f1e;border-radius:3px}
</style>
</head>
<body>
<div class="abs brand">Tall Beacons</div>

<nav class="abs main-nav">
  <div class="col" style="left:16px"><a class="current">Home</a><a>Two Minute Guide</a><a>About our analyses</a></div>
  <div class="sep" style="left:193px"></div>
  <div class="col" style="left:207px"><a>Current &amp; year to date performance</a><a>Watch list</a><a>Other key numbers</a></div>
  <div class="sep" style="left:495px"></div>
  <div class="col" style="left:505px"><a>About value investing</a><a>Back tested results</a><a>The Rowan 1000 and the T&amp;Q 500 index</a></div>
  <div class="sep" style="left:808px"></div>
  <div class="col" style="left:816px"><a>FAQs</a></div>
</nav>

<section class="abs hero" role="img" aria-label="Close-up photograph of a hand placing a coin into dark soil">
  <div class="abs util"><span>Login</span><i>|</i><span>Register for free</span><i>|</i><span>Contact us</span><i>|</i><span>Terms &amp; Conditions</span></div>
  <h1 class="abs">A potential return of 23.57 % a year<br>from America’s biggest businesses<br>with the emphasis firmly on<br>capital preservation.</h1>
  <div class="abs cta">Free Registration</div>
</section>

<section class="abs intro">
  <h2>Something Different!</h2>
  <p>You may well be thinking that Tall Beacons is just another one of those banal share recommendation sites sprinkled with the usual idiotic and patronising platitudes, gross exaggerations, silly get-rich-quick promises and all the other stuff and nonsense you associate with the black art of share-tipping...</p>
</section>

<article class="abs feature" style="left:8px;width:372px">
  <h3><svg width="16" height="24" viewBox="0 0 16 24"><path d="M8 1a7 7 0 0 0-4 12.7V17h8v-3.3A7 7 0 0 0 8 1z" fill="none" stroke="#333" stroke-width="1.5"/><path d="M5 19h6M6 22h4" stroke="#333" stroke-width="1.5"/></svg>Why Choose Us</h3>
  <p>Our program finds stocks that appear to be under-valued - i.e., where the price of a company’s share does not reflect the real worth of the business.</p>
  <span class="more">Read more...</span>
</article>

<article class="abs feature" style="left:416px;width:360px">
  <h3><svg width="26" height="22" viewBox="0 0 26 22"><path d="M1 21h24" stroke="#333" stroke-width="2"/><rect x="3" y="4" width="4" height="16" fill="#333"/><rect x="10" y="10" width="4" height="10" fill="#333"/><rect x="17" y="13" width="4" height="7" fill="#333"/></svg>How The Service works</h3>
  <p>Our software analyses 1,000 US stocks on the first day of every month looking for stocks where the key fundamentals are as we require. (See About our analyses) Once found, those stocks are added to our Watch list.</p>
  <span class="more">Read more...</span>
</article>

<aside class="abs signup">
  <h4>Free Registration</h4>
  <p><span class="trial">Free trial period:</span><br>if you would like to monitor the portfolio's per-formance for six months free of charge then please <span class="link">complete the registration form</span>.</p>
  <div class="abs register">Register Me Free<span class="arrow"><svg width="16" height="22" viewBox="0 0 16 22"><path d="M3 2l10 9-10 9" fill="none" stroke="#fff" stroke-width="3"/></svg></span></div>
</aside>

<footer class="abs site-map">
  <div>Navigate here:</div>
  <div>Home / Two minute guide / Current &amp; year to date performance / Watch list / Other key numbers / Back tested results / History of all trades /<br>About our analyses / About value investing / The Rowan 1000 and the T&amp;Q 500 index / FAQs</div>
  <div class="q">Do you have any Questions?<br>Please feel free to e-mail us at: info@tallbeacons.co.uk.</div>
  <div class="mark">Tall Beacons</div>
</footer>

<div class="abs legal">© Tall Beacons Ltd 2011. All rights reserved.&nbsp; Use of this website constitutes acceptance of our <u>User Agreement and Privacy Policy</u>.
  <div class="social"><span></span><span></span><span></span><span></span></div>
</div>
</body>
</html>
```